Door Hanger Design for Electricians Serving Homes

I would like our logo incorporated into the door hanger. We would like a place for a tear off section on the bottom of the hanger with our contact information: K&T Electric - (555) 318-4702 - www.kandtelectric.example - info@kandtelectric.example.
Door Hanger Script
Front Side of the Door Hanger:
[Company Logo]
Need a Reliable Electrician?
Your Local Electrical Expert is Just Around the Corner!
• Quick Response Times
• Affordable Rates
• Quality Workmanship
• Fully Licensed & Insured
• Special Offer:
• 10% OFF Your First Service Call!
Back Side of the Door Hanger:
Don't Let Electrical Issues Keep You in the Dark!
From flickering lights to complete system upgrades, we've got all your
residential electrical needs covered. Our services include:
• Electrical Repairs & Troubleshooting
• Lighting Installation & Upgrades
• Safety Inspections & Code Compliance
• Energy-Efficient Solutions
• 24/7 Emergency Services
• Why Choose Us?
• Friendly, Local Service
• Over 30 Years of Experience
• Satisfaction Guaranteed
• Upfront Pricing
Call Us Today: [Your Phone Number]
Visit Our Website: [Your Website]
Book Your Appointment Now and Claim Your 10% Discount!
Offer valid for new customers on the first visit only. Mention this door hanger when
booking.
[Your Company Name and Contact Information]
Follow Us on Social Media for More Tips and Special Offers!
[Icons for social media platforms: Chatterpage, Pixmosaic, Quibbler, etc.]
Design Tips:
Use bold, clear fonts for easy reading.
Incorporate your brand colors and logo for instant recognition.
Include a clear call to action (CTA) on both sides.
Add a tear-off section at the bottom with your contact information for
convenience.
Use high-quality images or graphics related to electrical work to catch
the eye.
This door hanger design and copy aim to attract residential clients by
highlighting the benefits of your electrical services, special offers, and
how they can easily get in touch with you for their electrical needs.
The door knocker template will have three of the same design on front and three of the same design on the back. This template is from the print shop.

```html
<!DOCTYPE html>
<html lang="en">
<head>
<meta charset="utf-8">
<title>K&amp;T Electric Door Hanger</title>
<link href="https://fonts.googleapis.com/css2?family=Oswald:wght@500;600;700&family=Nunito+Sans:wght@400;600;700;800&display=swap" rel="stylesheet">
<style>
:root{
  --bg:#c3c1c2;
  --red:#e21d24;
  --black:#0b0b0b;
  --white:#ffffff;
  --ink:#1a1a1a;
  --sky-top:#3f86d4;
  --sky-bottom:#1d3d7a;
  --bulb-dark:#1c0f08;
  --bulb-glow:#a8621c;
}
*{margin:0;padding:0;box-sizing:border-box}
html,body{width:1200px;height:904px;overflow:hidden;background:var(--bg)}
body{position:relative;font-family:"Nunito Sans",sans-serif;color:var(--ink)}
.hanger{position:absolute;top:55px;width:340px;height:794px;background:var(--white);overflow:hidden}
.hanger--front{left:238px}
.hanger--back{left:622px}
.hanger__art{position:absolute;inset:0}
.hanger__hole{position:absolute;width:108px;height:108px;border-radius:50%;background:var(--bg);left:117px;top:50px}
.photo-city{position:absolute;left:0;top:0;width:340px;height:570px;background:linear-gradient(180deg,var(--sky-top) 0%,#2f6fc0 45%,var(--sky-bottom) 78%,#3a2a1e 100%)}
.photo-bulbs{position:absolute;left:0;top:0;width:340px;height:350px;background:radial-gradient(circle at 35% 30%,#c98a3a 0%,transparent 30%),radial-gradient(circle at 68% 75%,var(--bulb-glow) 0%,transparent 35%),var(--bulb-dark)}
.abs{position:absolute}
.brand{left:0;width:340px;top:186px;text-align:center;font-family:"Oswald",sans-serif;font-weight:600;font-size:27px;color:var(--black);letter-spacing:.5px}
.headline{font-family:"Oswald",sans-serif;font-weight:500;line-height:1.2;letter-spacing:-.3px}
.headline--red{color:var(--red)}
.tagline{color:var(--red);font-weight:800;font-size:13.5px;line-height:18px}
.ticks{list-style:none}
.ticks li{position:relative;padding-left:15px;white-space:nowrap}
.ticks li::before{content:"";position:absolute;left:0;top:50%;width:10px;height:10px;margin-top:-5px;border-radius:50%;border:2px solid var(--red);background:radial-gradient(circle,var(--red) 0 2px,transparent 2.5px)}
.ticks--bold li{font-weight:700;font-size:12.5px;line-height:19px}
.ticks--light li{font-size:12px;line-height:19px}
.label{color:var(--red);font-weight:800}
.contact{color:var(--white);font-size:13.5px;line-height:20px}
.contact__row{display:flex;align-items:center;gap:6px}
.contact__row svg{flex:none}
.intro{font-weight:700;font-size:11.3px;line-height:15px;color:var(--black)}
.fineprint{text-align:center;font-size:9.5px;line-height:13px;color:var(--ink)}
.fineprint strong{color:var(--red);font-weight:800;display:block}
.social{display:flex;flex-direction:column;gap:2px;color:var(--white);font-size:8.5px;font-weight:700}
.social span{display:flex;align-items:center;gap:4px}
.social span::before{content:"";width:7px;height:7px;background:var(--white)}
</style>
</head>
<body>

<section class="hanger hanger--front" aria-label="Door hanger front">
  <div class="photo-city" role="img" aria-label="Photo of a city skyline at dusk with lit towers"></div>
  <svg class="hanger__art" width="340" height="794" viewBox="0 0 340 794" aria-hidden="true">
    <polygon points="0,445 340,565 340,794 0,794" fill="var(--white)"/>
    <polygon points="0,438 182,467 118,490 262,512 208,533 340,552 340,566 192,541 248,520 96,494 160,472 0,447" fill="var(--red)"/>
    <polygon points="0,672 164,704 140,720 245,746 218,760 340,770 340,794 0,794" fill="var(--black)"/>
    <polyline points="0,669 164,701 140,717 245,743 218,757 340,767" fill="none" stroke="var(--red)" stroke-width="3"/>
  </svg>
  <div class="hanger__hole"></div>
  <div class="abs brand">K&amp;T Electric, LLC</div>

  <h1 class="abs headline" style="left:24px;top:493px;font-size:24px">Need a<br>Reliable Electrician?</h1>
  <p class="abs tagline" style="left:24px;top:553px">Your Local Electrical Expert is Just<br>Around the Corner!</p>
  <ul class="abs ticks ticks--bold" style="left:24px;top:591px">
    <li>Quick Response Times</li>
    <li>Affordable Rates</li>
    <li>Quality Workmanship</li>
    <li>Fully Licensed &amp; Insured</li>
  </ul>

  <svg class="abs offer-badge" style="left:204px;top:566px" width="120" height="170" viewBox="0 0 120 170" aria-label="Special offer: 10% off your first service call">
    <path id="arcSpecial" d="M4,78 A64 64 0 0 1 116,78" fill="none" stroke="var(--red)" stroke-width="20"/>
    <path id="arcOffer" d="M20,92 A46 46 0 0 1 100,92" fill="none" stroke="var(--red)" stroke-width="17"/>
    <text font-family="Oswald,sans-serif" font-weight="700" font-size="17" fill="var(--white)" dy="6"><textPath href="#arcSpecial" startOffset="50%" text-anchor="middle">SPECIAL</textPath></text>
    <text font-family="Oswald,sans-serif" font-weight="700" font-size="15" fill="var(--white)" dy="5"><textPath href="#arcOffer" startOffset="50%" text-anchor="middle">OFFER</textPath></text>
    <circle cx="60" cy="128" r="48" fill="var(--red)"/>
    <circle cx="60" cy="128" r="50" fill="none" stroke="var(--red)" stroke-width="5" stroke-dasharray="3.5 3.5"/>
    <circle cx="60" cy="128" r="41" fill="var(--black)" stroke="var(--white)" stroke-width="2"/>
    <text x="52" y="131" text-anchor="middle" font-family="Oswald,sans-serif" font-weight="700" font-size="30" fill="var(--white)">10</text>
    <text x="80" y="118" text-anchor="middle" font-family="Oswald,sans-serif" font-weight="600" font-size="16" fill="var(--white)">%</text>
    <text x="80" y="131" text-anchor="middle" font-family="Oswald,sans-serif" font-weight="600" font-size="10" fill="var(--white)">OFF</text>
    <text x="60" y="146" text-anchor="middle" font-family="Nunito Sans,sans-serif" font-weight="800" font-size="8.5" fill="var(--white)">Your First</text>
    <text x="60" y="157" text-anchor="middle" font-family="Nunito Sans,sans-serif" font-weight="800" font-size="8.5" fill="var(--white)">Service Call!</text>
  </svg>

  <div class="abs contact" style="left:24px;top:696px">
    <div class="label" style="font-size:14px">CONTACT US</div>
    <div class="contact__row"><svg width="13" height="13" viewBox="0 0 13 13"><circle cx="6.5" cy="6.5" r="6.5" fill="var(--red)"/><path d="M4 3.5l1.3-.3.8 1.8-.8.6a4 4 0 002 2l.6-.8 1.8.8-.3 1.3C6.5 9 4 6.5 4 3.5z" fill="var(--white)"/></svg>(555) 318-4702</div>
    <div class="contact__row"><svg width="13" height="13" viewBox="0 0 13 13"><circle cx="6.5" cy="6.5" r="6.5" fill="var(--red)"/><rect x="3.5" y="4.5" width="6" height="4.2" fill="none" stroke="var(--white)" stroke-width=".9"/><path d="M3.5 4.5l3 2.3 3-2.3" fill="none" stroke="var(--white)" stroke-width=".9"/></svg>info@kandtelectric.example</div>
    <div class="contact__row"><svg width="13" height="13" viewBox="0 0 13 13"><circle cx="6.5" cy="6.5" r="5.6" fill="none" stroke="var(--red)" stroke-width="1.4"/><ellipse cx="6.5" cy="6.5" rx="2.3" ry="5.6" fill="none" stroke="var(--red)" stroke-width="1"/><path d="M1 6.5h11" stroke="var(--red)" stroke-width="1"/></svg>www.kandtelectric.example</div>
  </div>
</section>

<section class="hanger hanger--back" aria-label="Door hanger back">
  <div class="photo-bulbs" role="img" aria-label="Photo of glowing filament light bulbs hanging in the dark"></div>
  <svg class="hanger__art" width="340" height="794" viewBox="0 0 340 794" aria-hidden="true">
    <polygon points="0,229 340,344 340,794 0,794" fill="var(--white)"/>
    <polygon points="0,226 130,266 118,287 276,302 209,323 340,338 340,346 200,330 262,308 104,294 116,274 0,236" fill="var(--red)"/>
    <polygon points="0,619 163,652 145,680 245,695 215,716 340,725 340,794 0,794" fill="var(--black)"/>
    <polyline points="0,616 163,649 145,677 245,692 215,713 340,722" fill="none" stroke="var(--red)" stroke-width="3"/>
  </svg>
  <div class="hanger__hole"></div>

  <h2 class="abs headline" style="left:24px;top:270px;font-size:24px;line-height:29px">
    <span class="headline--red">Don't Let</span><br>Electrical Issues<br><span class="headline--red">Keep You in the Dark!</span>
  </h2>
  <p class="abs intro" style="left:24px;top:370px">From flickering lights to complete system upgrades,<br>we've got all your residential electrical needs covered.</p>
  <div class="abs label" style="left:24px;top:403px;font-size:12px">Our services include:</div>
  <ul class="abs ticks ticks--light" style="left:24px;top:416px">
    <li>Electrical Repairs &amp; Troubleshooting</li>
    <li>Lighting Installation &amp; Upgrades</li>
    <li>Safety Inspections &amp; Code Compliance</li>
    <li>Energy-Efficient Solutions</li>
    <li>24/7 Emergency Services</li>
  </ul>
  <div class="abs label" style="left:24px;top:522px;font-size:12px">Why Choose Us?</div>
  <ul class="abs ticks ticks--light" style="left:24px;top:539px">
    <li>Friendly, Local Service</li>
    <li>Over 30 Years of Experience</li>
    <li>Satisfaction Guaranteed</li>
    <li>Upfront Pricing</li>
  </ul>

  <svg class="abs cta-badge" style="left:206px;top:496px" width="110" height="110" viewBox="0 0 110 110" aria-label="Book your appointment now and claim your 10% discount">
    <circle cx="55" cy="55" r="49" fill="var(--red)"/>
    <circle cx="55" cy="55" r="51" fill="none" stroke="var(--red)" stroke-width="5" stroke-dasharray="3.5 3.5"/>
    <circle cx="55" cy="55" r="42" fill="var(--black)" stroke="var(--white)" stroke-width="2"/>
    <g font-family="Oswald,sans-serif" font-weight="500" font-size="10.5" text-anchor="middle" fill="var(--white)">
      <text x="55" y="38">Book Your</text>
      <text x="55" y="51">Appointment</text>
      <text x="55" y="64">Now &amp; Claim Your</text>
      <text x="55" y="77" fill="var(--red)">10% Discount!</text>
    </g>
  </svg>
  <p class="abs fineprint" style="left:196px;top:608px;width:130px"><strong>OFFER VALID FOR<br>NEW CUSTOMERS</strong>on the first visit only.<br>Mention this door<br>hanger when booking.</p>

  <div class="abs contact" style="left:24px;top:655px;font-size:12.5px;line-height:16px">
    <div class="label">Call Us Today:</div>
    <div class="contact__row"><svg width="12" height="12" viewBox="0 0 13 13"><circle cx="6.5" cy="6.5" r="6.5" fill="var(--red)"/><path d="M4 3.5l1.3-.3.8 1.8-.8.6a4 4 0 002 2l.6-.8 1.8.8-.3 1.3C6.5 9 4 6.5 4 3.5z" fill="var(--white)"/></svg>(555) 318-4702</div>
    <div class="label" style="margin-top:11px">Visit Our Website:</div>
    <div class="contact__row"><svg width="12" height="12" viewBox="0 0 13 13"><circle cx="6.5" cy="6.5" r="5.6" fill="none" stroke="var(--red)" stroke-width="1.4"/><ellipse cx="6.5" cy="6.5" rx="2.3" ry="5.6" fill="none" stroke="var(--red)" stroke-width="1"/><path d="M1 6.5h11" stroke="var(--red)" stroke-width="1"/></svg>www.kandtelectric.example</div>
    <div class="label" style="margin-top:10px">Follow Us on Social Media<br>or More Tips and Special Offers!</div>
  </div>
  <div class="abs social" style="left:256px;top:745px">
    <span>Chatterpage</span>
    <span>Pixmosaic</span>
    <span>Quibbler</span>
  </div>
</section>

</body>
</html>
```